Either a trifold or double sided flyer/brochure

A flyer to help spark interest in a historic preservation project in Alderbrook, NH--looking for something that captures the early 19th century rural village and mill times--American Primitive, Shaker, Cross Stitch Sampler...must be able to highlight home history as well as have all owners of house on a single page. Word document attached--can also provide files for the house painting, color photos, dunby photo, advertising photo or part of original settler map.
I like this brochure
http://tovabrenick.com/wordpress/pell-barn-museum-brochure/
community stakeholders, residents,
Historic Preservation, House Museums.

```html
<!DOCTYPE html>
<html lang="en">
<head>
<meta charset="utf-8">
<title>Hartwell Homestead Brochure</title>
<link href="https://fonts.googleapis.com/css2?family=Oswald:wght@500&family=Arimo:wght@400;700&display=swap" rel="stylesheet">
<style>
:root{
  --navy:#13243a;
  --gold:#c98a2e;
  --heading:#b4702a;
  --paper:#f4efe9;
  --paper-edge:#e9e1d8;
  --ink:#1e1e1e;
  --rule:#c9bfb3;
  --backdrop:#d9d9d9;
}
*{box-sizing:border-box;margin:0;padding:0}
html,body{width:813px;height:1200px;overflow:hidden;background:var(--backdrop)}
.canvas{position:relative;width:813px;height:1200px;overflow:hidden;background:var(--backdrop);font-family:"Arimo",Arial,sans-serif;color:var(--ink)}
.spread{position:absolute;left:76px;width:652px;height:506px;background:linear-gradient(90deg,var(--paper),#faf7f3 50%,var(--paper));overflow:hidden;box-shadow:0 3px 10px rgba(0,0,0,.25)}
.spread--outer{top:78px}
.spread--inner{top:642px}
.panel{position:absolute;top:0;height:100%}
.fold{position:absolute;top:0;width:1px;height:100%;background:rgba(0,0,0,.08)}
.photo{position:absolute}
.band{position:absolute;left:0;bottom:0;width:100%;height:64px}
.group-link{position:absolute;display:flex;align-items:center;gap:6px;font-size:7px;color:var(--gold)}
.group-link .dot{width:20px;height:20px;border-radius:50%;background:var(--gold);flex:none}
.section-title{font-family:"Oswald",sans-serif;font-weight:500;color:var(--heading);text-transform:uppercase;letter-spacing:-.2px;line-height:1.05}
.owners{position:absolute;left:18px;top:197px;width:185px;list-style:none}
.owners li{display:flex;justify-content:space-between;align-items:center;height:21px;border-bottom:1px dotted var(--rule);font-size:5.4px;line-height:1.2}
.owners .yr{color:var(--gold);flex:none;width:36px}
.snap{position:absolute;background:#fff;padding:5px;box-shadow:0 2px 5px rgba(0,0,0,.3)}
.snap div{width:100%;height:100%}
.center-caption{position:absolute;text-align:center;font-size:9px;line-height:1.6}
.cover-title{position:absolute;left:426px;width:226px;top:372px;text-align:center;color:#fff;font-family:"Oswald",sans-serif;font-weight:500;font-size:17px;text-transform:uppercase}
.cover-address{position:absolute;left:426px;width:226px;top:404px;text-align:center;color:#fff;font-size:10.5px;line-height:1.55}
.history{position:absolute;left:20px;top:142px;width:482px}
.history h2{font-size:12px;margin-bottom:7px}
.history p{font-size:6.4px;line-height:1.24;text-align:justify;margin-bottom:6.5px;width:402px}
</style>
</head>
<body>
<div class="canvas">

  <!-- Outer side: owners, centre panel, cover -->
  <section class="spread spread--outer">
    <div class="panel" style="left:0;width:211px">
      <div class="photo" role="img" aria-label="Photograph of the yellow clapboard homestead gable under bare trees and blue sky" style="left:0;top:0;width:211px;height:147px;background:linear-gradient(115deg,#d9ad45 0%,#e5bd55 50%,#3c6db5 80%,#2f5ea8 100%)"></div>
      <h2 class="section-title" style="position:absolute;left:18px;top:163px;font-size:8px">Owners of 47 Mill Pond Road<br>Alderbrook, New Hampshire</h2>
      <ul class="owners">
        <li><span>Robert Greene (grandson of John Greene) owned the land</span><span class="yr">1826</span></li>
        <li><span>George S. Hartwell and Jane (Barlow) Hartwell</span><span class="yr">1826-1828</span></li>
        <li><span>Deacon Thomas Prentice and Alice (Lowell) Prentice (Baptist)</span><span class="yr">1828-1839</span></li>
        <li><span>Elijah Brown Sawyer and Achsah (Pratt) Sawyer<br>(mortgage between Samuel Lowell and Sawyer in 1845)</span><span class="yr">1839-1877</span></li>
        <li><span>Mary Ellen Sawyer</span><span class="yr">1877-1898</span></li>
        <li><span>James Corliss</span><span class="yr">1898-1904</span></li>
        <li><span>Fred Parker Dunby and Grace E. (Holloway) Dunby</span><span class="yr">1904-1956</span></li>
        <li><span>Elinor (Dunby) Whitcomb and Frank O Whitcomb<br>(Elinor was born in house on July 29, 1911)</span><span class="yr">1955-1998</span></li>
        <li><span>James H. Vandermeer and Maria Soto Vandermeer<br>(James was nephew of Elinor (Dunby) Whitcomb)</span><span class="yr">1998-2015</span></li>
        <li><span>Brookhaven</span><span class="yr">2015-2022</span></li>
        <li><span>Edward M. Castellano and Albert A. Pemberton, Jr.</span><span class="yr">2022</span></li>
      </ul>
    </div>

    <div class="fold" style="left:211px"></div>

    <div class="panel" style="left:211px;width:215px">
      <div class="photo" role="img" aria-label="Photograph of the old wooden staircase inside the homestead" style="left:0;top:0;width:215px;height:147px;background:linear-gradient(150deg,#f1ece4 0%,#c99b6a 45%,#8a5a35 75%,#e8e2d8 100%)"></div>
      <div class="snap" style="left:20px;top:190px;width:115px;height:90px;transform:rotate(5deg)">
        <div role="img" aria-label="Photograph of an empty room with patterned wallpaper" style="background:linear-gradient(180deg,#d8d0c4 0%,#c4b9aa 60%,#6b3a33 100%)"></div>
      </div>
      <div class="snap" style="left:85px;top:233px;width:125px;height:95px;transform:rotate(8deg)">
        <div role="img" aria-label="Photograph of a brick fireplace in the parlour" style="background:linear-gradient(160deg,#c9b7a3 0%,#8a4e34 50%,#5c2e22 100%)"></div>
      </div>
      <h2 class="section-title" style="position:absolute;left:0;width:215px;top:338px;text-align:center;font-size:11.5px">Hartwell Homestead c. 1826,</h2>
      <p class="center-caption" style="left:0;width:215px;top:355px">Dunbys Corner, Alderbrook,<br>New Hampshire</p>
    </div>

    <div class="fold" style="left:426px"></div>

    <div class="photo" role="img" aria-label="Photograph of the yellow homestead among autumn trees" style="left:426px;top:0;width:226px;height:460px;background:linear-gradient(180deg,#7a6a2a 0%,#b08a3a 22%,#c79a3f 45%,#6b5526 68%,#3a2c17 100%)"></div>
    <p class="cover-title">Hartwell Homestead</p>
    <p class="cover-address">47 Mill Pond Road<br>Alderbrook, New Hampshire</p>

    <svg class="band" viewBox="0 0 652 64" preserveAspectRatio="none" aria-hidden="true">
      <path fill="var(--navy)" d="M0 12 L20 8 L38 13 L60 9 L82 14 L104 10 L128 13 L150 8 L172 12 L196 9 L211 13 L232 8 L256 12 L280 9 L300 13 L324 8 L348 12 L372 10 L396 14 L426 9 L448 13 L470 8 L494 12 L518 9 L542 13 L566 8 L590 12 L614 9 L636 13 L652 9 L652 64 L0 64 Z"/>
    </svg>
    <p class="group-link" style="left:22px;top:478px"><span class="dot"></span>They invite you to join their Gatherbook Group</p>
    <p class="group-link" style="left:233px;top:478px"><span class="dot"></span>They invite you to join their Gatherbook Group</p>
    <p class="group-link" style="left:448px;top:478px"><span class="dot"></span>They invite you to join their Gatherbook Group</p>
  </section>

  <!-- Inner side: history and archive panel -->
  <section class="spread spread--inner">
    <div class="photo" role="img" aria-label="Photograph of the homestead and barn in winter snow" style="left:0;top:0;width:432px;height:131px;background:linear-gradient(180deg,#cfd2d4 0%,#d4b25a 40%,#9b8a6a 65%,#f2f2f2 85%,#fafafa 100%)"></div>

    <article class="history">
      <h2 class="section-title">The Hartwell Homestead History c. 1826</h2>
      <p>In 1826, George S. Hartwell and his wife, Jane (Barlow) Hartwell purchased 26 acres from Robert Greene on the Kettlebrook River, north of Fenwick's Woolen Mill in South Alderbrook, NH. This parcel was carved out lot #32 which was comprised of 268 acres that were deeded to John Greene (Robert Greene's grandfather) by Jeremiah Ashby and John Crane on May 5, 1762.</p>
      <p>It is believed that Hartwell, who was blacksmith, built the house that currently stands at 47 Mill Pond Road in Alderbrook, NH. He also built his forge on the site down by the river. It is likely that much of the forged hardware in the home was crafted by him. Feeling the need to leave Alderbrook for a new frontier, Hartwell left town with his brother, Silas, to purchase land in the emerging communities of Larch County, NY. Before doing so, Hartwell sold the home, shop and buildings to Thomas Prentice and his wife Alice (Lowell) Prentice in 1828.</p>
      <p>By trade, Thomas Prentice was a cloth dresser and wool-carder. He was also a deeply religious man and served as deacon in the emerging, but still quite small, Baptist community. In those days, small groups of the Baptists and Methodists met in the Ridley Home for bible study, prayers and singing. The Ridleys were well known abolitionists and their house served as a stop on the Underground Railroad. Deacon Prentice died in 1839 and his estate was managed by Samuel Lowell&mdash;very likely a relative of Alice&mdash;who protected Alice's dower. The property was then sold to Elijah Brown Sawyer and his wife Achsah (Pratt) Sawyer. Elijah was quite industrious and continued to expand the wool mill. He was an early investor in the Granite Ridge Railroad and ceded a right of way to the railroad on the homestead. The mill eventually came under the control of his son, Henry A. Sawyer, and operated until it burned down on April 20, 1874. Elijah passed away in 1877 and left the home to Mary Ellen Sawyer who was most commonly known as &ldquo;Ellen.&rdquo;</p>
      <p>Ellen Sawyer was approached in 1891 by Allie Fenwick, the owner of the Fenwick's Mill Complex, to ask if she would be willing to rent out the home to a couple from Boston. This turned out to be Marian and Edward Thornbury, the founders of the Thornbury Colony, who ended up spending their first summer in Alderbrook, NH in the home. Marian recalls in her writings: &ldquo;You can't fail to remember the two-story farmhouse almost across from the road from the iron bridge, now occupied by the Dunby Family. It had never been painted and was a lovely soft gray in color. There were really only four rooms and a kitchen, spotlessly clean and adequately furnished, which really didn't mean much but some chairs, tables and beds. Then in the kitchen was something that fascinated me, a stone bowl into which the clearest of water was all the time pouring and then running off into a a drain&hellip;.&rdquo;</p>
      <p>The Dunbys lived in this home for the longest time of any owner&ndash;and some refer to this area before the bridge, as Dunbys Corner. This moment of stewardship began under Fred Parker Dunby and his wife Grace E. (Holloway) Dunby around 1904 and lasted until 2015 when a descendant sold the home. The house is now under the stewardship of Edward M. Castellano and Albert A. Pemberton, Jr. and will be undergoing a significant restoration.</p>
    </article>

    <div class="fold" style="left:432px"></div>

    <div class="panel" style="left:432px;width:220px">
      <div class="photo" role="img" aria-label="Painting of the white homestead and barn under a blue sky" style="left:0;top:0;width:220px;height:131px;background:linear-gradient(180deg,#5b7fb0 0%,#3f6390 40%,#2f4a3a 70%,#27405e 100%)"></div>
      <div class="snap" style="left:4px;top:162px;width:112px;height:92px;transform:rotate(-8deg)">
        <div role="img" aria-label="Sepia portrait photograph of a woman from the Thornbury household" style="background:linear-gradient(160deg,#cbbfa8 0%,#8c7a5e 55%,#4a3d2c 100%)"></div>
      </div>
      <div class="snap" style="left:104px;top:130px;width:112px;height:92px;transform:rotate(8deg)">
        <div role="img" aria-label="Sepia photograph of Fred and Grace Dunby" style="background:linear-gradient(160deg,#d2c6b0 0%,#7e6d55 55%,#3f3426 100%)"></div>
      </div>
      <p class="center-caption" style="left:0;width:220px;top:258px;font-size:8px;line-height:1.6">Hartwell Homestead c. 1826,<br>Dunbys Corner, Alderbrook,<br>New Hampshire</p>
      <div role="img" aria-label="Section of the early settler map showing lots near the mill" style="position:absolute;left:55px;top:302px;width:114px;height:107px;background:linear-gradient(135deg,#e6e3dc,#cfcac0);border:1px solid #b9b2a6"></div>
      <div role="img" aria-label="Old newspaper advertisement for a wool carder and cloth dresser" style="position:absolute;left:83px;top:423px;width:62px;height:42px;background:linear-gradient(180deg,#ece8e0,#d8d2c6)"></div>
    </div>

    <svg class="band" viewBox="0 0 652 64" preserveAspectRatio="none" aria-hidden="true" style="height:40px">
      <path fill="var(--navy)" d="M0 10 L24 6 L46 11 L70 7 L94 12 L118 8 L142 11 L166 6 L190 10 L214 7 L238 11 L262 6 L286 10 L310 7 L334 11 L358 6 L382 10 L406 7 L432 11 L456 6 L480 10 L504 7 L528 11 L552 6 L576 10 L600 7 L626 11 L652 7 L652 64 L0 64 Z"/>
    </svg>
    <p class="group-link" style="left:22px;top:483px"><span class="dot"></span>They invite you to join their Gatherbook Group</p>
  </section>

</div>
</body>
</html>
```